Business Card Design

We are looking for a business card designed for our landscaping company. We do landscaping installation & Maintenance Services. We would like to see designs that have basic landscaping in background. We also think it is important to have both of our names and phone numbers on the card. We need something that stands out a little whether it is shape of the card or thickness or design.

Industry/Entity Type

Business

Contact Information for Business Card

Pale Ridge Yardworks, paleridgeyardworks@mailbrook.net, Dale Purvine 555-213-7690, Martin Kolbey 555-864-1037

```html
<!DOCTYPE html>
<html lang="en">
<head>
<meta charset="utf-8">
<title>Pale Ridge Yardworks – Business Card</title>
<link rel="stylesheet" href="https://fonts.googleapis.com/css2?family=Open+Sans:wght@400;600;700&display=swap">
<style>
  :root {
    --navy: #1f3580;
    --navy-deep: #172a6a;
    --card-white: #f7f8fb;
    --page: #e6e8ee;
    --text-light: #ffffff;
  }
  * { margin: 0; padding: 0; box-sizing: border-box; }
  html, body {
    width: 1200px;
    height: 800px;
    overflow: hidden;
    background: var(--page);
    font-family: "Open Sans", Arial, sans-serif;
  }
  .card {
    position: absolute;
    left: 75px;
    top: 100px;
    width: 1050px;
    height: 600px;
    background: var(--card-white);
    overflow: hidden;
    box-shadow: 0 10px 30px rgba(20, 30, 70, 0.18);
  }
  .card-shapes {
    position: absolute;
    inset: 0;
  }
  .company-name {
    position: absolute;
    left: 100px;
    top: 90px;
    font-size: 34px;
    font-weight: 600;
    line-height: 1.2;
    color: var(--navy);
    letter-spacing: 0.2px;
  }
  .company-email {
    position: absolute;
    left: 100px;
    top: 160px;
    display: flex;
    align-items: center;
    gap: 10px;
    font-size: 24px;
    color: var(--navy);
  }
  .contacts {
    position: absolute;
    left: 640px;
    top: 238px;
    color: var(--text-light);
  }
  .contact + .contact { margin-top: 38px; }
  .contact-name {
    font-size: 31px;
    font-weight: 600;
    line-height: 1.2;
  }
  .contact-phone {
    display: flex;
    align-items: center;
    gap: 8px;
    font-size: 30px;
    font-weight: 600;
    line-height: 1.3;
  }
  .icon { flex: none; }
  .plant-art {
    position: absolute;
    left: 30px;
    top: 360px;
    width: 170px;
    height: 240px;
    background: linear-gradient(180deg, rgba(31,53,128,0.15) 0%, rgba(31,53,128,0.75) 100%);
  }
</style>
</head>
<body>
  <div class="card">
    <svg class="card-shapes" width="1050" height="600" viewBox="0 0 1050 600" aria-hidden="true">
      <path class="navy-field" fill="var(--navy)"
        d="M840,0 C800,120 560,170 400,250 C290,310 240,420 240,600 L1050,600 L1050,0 Z"/>
      <path class="top-swoosh" fill="var(--navy)"
        d="M0,200 C0,80 170,18 450,48 C200,30 20,60 16,205 Z"/>
      <path class="bottom-swoosh" fill="var(--card-white)"
        d="M580,525 C760,600 1000,560 1005,400 C1030,540 800,605 580,525 Z"/>
    </svg>

    <div class="plant-art" role="img" aria-label="Silhouette of a cattail and leafy grass plant"></div>

    <div class="company-name">Pale Ridge Yardworks</div>
    <div class="company-email">
      <svg class="icon" width="22" height="22" viewBox="0 0 22 22" aria-hidden="true">
        <circle cx="11" cy="11" r="11" fill="var(--navy)"/>
        <rect x="5" y="7" width="12" height="8" fill="none" stroke="#fff" stroke-width="1.5"/>
        <path d="M5,7 L11,12 L17,7" fill="none" stroke="#fff" stroke-width="1.5"/>
      </svg>
      <span>paleridgeyardworks@mailbrook.net</span>
    </div>

    <div class="contacts">
      <div class="contact">
        <div class="contact-name">Dale Purvine</div>
        <div class="contact-phone">
          <svg class="icon" width="28" height="28" viewBox="0 0 28 28" aria-hidden="true">
            <circle cx="14" cy="14" r="12" fill="none" stroke="#fff" stroke-width="2"/>
            <path d="M9,8 L11.5,7.5 L13,11 L11.5,12.5 C12.5,14.5 13.5,15.5 15.5,16.5 L17,15 L20.5,16.5 L20,19 C15,20 8,13 9,8 Z" fill="#fff"/>
          </svg>
          <span>555-213-7690</span>
        </div>
      </div>
      <div class="contact">
        <div class="contact-name">Martin Kolbey</div>
        <div class="contact-phone">
          <svg class="icon" width="28" height="28" viewBox="0 0 28 28" aria-hidden="true">
            <circle cx="14" cy="14" r="12" fill="none" stroke="#fff" stroke-width="2"/>
            <path d="M9,8 L11.5,7.5 L13,11 L11.5,12.5 C12.5,14.5 13.5,15.5 15.5,16.5 L17,15 L20.5,16.5 L20,19 C15,20 8,13 9,8 Z" fill="#fff"/>
          </svg>
          <span>555-864-1037</span>
        </div>
      </div>
    </div>
  </div>
</body>
</html>
```